wedding invitation card

Requirement:
1. White background, pink elements on the card, simple elegant looking
2. content:
Please join us as we celebrate new beginnings, new dreams,
and most importantly, new love at the marriage of
Miss Lin Qiao and Mr. Haoran Mu
Friday, The First of January
Two Thousand Fifteen at Eleven o’clock
Coral Tide Resort Palm Breeze Garden.

Reception will be followed at Lotus Hall at Half-Past Twelve o'clock

Please RSVP before December 18th 2015 by email: qiaolin0815@mailvexa.com

3. Flat paper
4. be able to change the size of the design according to printing requirement

Industry/Entity Type

Wedding

```html
<!DOCTYPE html>
<html lang="en">
<head>
<meta charset="utf-8">
<title>Wedding Invitation – Lin Qiao &amp; Haoran Mu</title>
<link rel="stylesheet" href="https://fonts.googleapis.com/css2?family=Pinyon+Script&family=Didact+Gothic&family=Playfair+Display:ital,wght@1,700&display=swap">
<style>
  :root {
    --backdrop: #d6d6d6;
    --paper: #ffffff;
    --edge: #a9a9a9;
    --lace-light: #fbeef4;
    --lace: #f2d3e2;
    --rose: #c973aa;
    --plum: #8a0f4c;
    --ink: #5a5a5a;
    --ink-soft: #6f6f6f;
    --rule: #8c8c8c;
    --fold-shade: #e4e4e4;
  }
  * { box-sizing: border-box; margin: 0; padding: 0; }
  html, body { width: 1200px; height: 738px; overflow: hidden; }
  body { background: var(--backdrop); position: relative; }

  .card {
    position: absolute;
    background: var(--paper);
    border: 1px solid var(--edge);
    overflow: hidden;
  }
  .card--front  { left: 86px;  top: 105px; width: 498px; height: 249px; }
  .card--back   { left: 93px;  top: 398px; width: 498px; height: 250px; }
  .card--inside { left: 623px; top: 74px;  width: 498px; height: 500px; }

  .lace-pattern { position: absolute; inset: 0; }
  .lace-pattern--full {
    background: radial-gradient(ellipse at 50% 45%, var(--lace) 0%, var(--lace-light) 70%, var(--paper) 100%);
  }
  .lace-pattern--fade {
    background: radial-gradient(ellipse at 55% 10%, var(--lace) 0%, var(--lace-light) 60%, var(--paper) 92%);
  }

  .front-title {
    position: absolute; left: 0; right: 0; top: 98px;
    text-align: center;
    font-family: "Pinyon Script", cursive;
    font-weight: 400;
    font-size: 52px; line-height: 1;
    color: var(--ink-soft);
  }

  .back-date {
    position: absolute; left: 99px; top: 213px;
    font-family: "Playfair Display", serif;
    font-style: italic; font-weight: 700;
    font-size: 10px; color: var(--plum);
  }

  .inside-fold {
    position: absolute; left: 0; right: 0; top: 0; height: 246px;
    border-bottom: 1px solid #ececec;
    background: linear-gradient(to bottom, var(--paper) 0%, var(--paper) 78%, var(--fold-shade) 100%);
  }

  .intro {
    position: absolute; left: 0; right: 0; top: 274px;
    text-align: center;
    font-family: "Didact Gothic", sans-serif;
    font-size: 12px; line-height: 15.5px; color: var(--ink);
  }

  .couple {
    position: absolute; left: 0; right: 0; top: 314px;
    text-align: center;
    font-family: "Pinyon Script", cursive;
    font-weight: 400;
    color: var(--rose);
  }
  .couple__name { display: block; font-size: 46px; line-height: 42px; }
  .couple__title { font-size: 22px; margin-right: 5px; }
  .couple__and { display: block; font-size: 22px; line-height: 12px; margin: -8px 0 -2px 0; }
  .couple__name--bride { margin-left: 10px; }
  .couple__name--groom { margin-left: -20px; }

  .details {
    position: absolute; left: 43px; top: 438px;
    display: flex; height: 42px;
    font-family: "Didact Gothic", sans-serif;
    font-size: 7.4px; line-height: 9.3px; color: var(--ink);
  }
  .details__col { padding-top: 1px; }
  .details__col--date  { width: 100px; }
  .details__col--venue { width: 187px; border-left: 1px solid var(--rule); padding-left: 16px; }
  .details__col--rsvp  { border-left: 1px solid var(--rule); padding-left: 11px; }
  .details p + p { margin-top: 9px; }
</style>
</head>
<body>

  <section class="card card--front" aria-label="Card front">
    <div class="lace-pattern lace-pattern--full" role="img" aria-label="Pale pink hand-drawn lace doodle pattern covering the card"></div>
    <h1 class="front-title">Invitation</h1>
  </section>

  <section class="card card--back" aria-label="Card back">
    <div class="lace-pattern lace-pattern--fade" role="img" aria-label="Pale pink hand-drawn lace doodle pattern fading toward the lower edge"></div>
    <p class="back-date">1.01.2016</p>
  </section>

  <section class="card card--inside" aria-label="Card inside">
    <div class="inside-fold"></div>

    <p class="intro">Please join us as we celebrate new beginnings, new dreams,<br>and most importantly, new love at the marriage of</p>

    <h2 class="couple">
      <span class="couple__name couple__name--bride"><span class="couple__title">miss</span>Lin Qiao</span>
      <span class="couple__and">and</span>
      <span class="couple__name couple__name--groom"><span class="couple__title">mr.</span>Haoran Mu</span>
    </h2>

    <div class="details">
      <div class="details__col details__col--date">
        FRIDAY,<br>THE FIRST OF JANUARY<br>Two Thousand Fifteen<br>at Eleven o'clock
      </div>
      <div class="details__col details__col--venue">
        <p>Coral Tide Resort Palm Breeze Garden.</p>
        <p>Reception will be followed<br>at Lotus Hall at Half-Past Twelve o'clock</p>
      </div>
      <div class="details__col details__col--rsvp">
        Please RSVP<br>before December 18th 2015<br>by email: qiaolin0815@mailvexa.com
      </div>
    </div>
  </section>

</body>
</html>
```